Rack Card for Portuguese Walking Food Tour

I would like a vertical rack card measuring 99x210mm. Here is the information I would like to include. It does not need to be in this format. We are located in Setubal, Portugal.
Please use the attached Blue Kite Emblem.
Setúbal: Tradition and Today
Experience the culinary delights of Setúbal, Portugal with a walking food tour around our waterfront village. Discover the Mercado do Salgueiral, voted one of the world’s best markets by Daily Meridian, and indulge in local wines and dishes. Prepare for a calm stroll on flat streets. No hills to climb on this tour.
Duration: 4 hours
www.brisklanepasseios.com
+351 265 847 390

```html
<!DOCTYPE html>
<html lang="en">
<head>
<meta charset="utf-8">
<title>Setúbal Rack Card</title>
<link rel="stylesheet" href="https://fonts.googleapis.com/css2?family=Baloo+2:wght@800&family=Patrick+Hand+SC&family=Poppins:wght@600&display=swap">
<style>
  :root {
    --backdrop: #666666;
    --map-grey: #ebebeb;
    --paper: #ffffff;
    --orange: #f26522;
    --ink: #111111;
    --brand-grey: #55575a;
    --photo-top: #e2e3e5;
    --photo-mid: #cfd1d4;
    --photo-low: #bcbfc3;
  }
  * { box-sizing: border-box; margin: 0; padding: 0; }
  html, body { width: 1200px; height: 1197px; overflow: hidden; }
  body { background: var(--backdrop); position: relative; font-family: "Poppins", sans-serif; font-weight: 600; }

  .rack-card {
    position: absolute; top: 30px; width: 535px; height: 1136px;
    overflow: hidden; color: var(--ink);
  }
  .rack-card--plain { left: 33px; }
  .rack-card--photo { left: 632px; }

  .city-map { position: absolute; inset: 0; background: var(--map-grey); }
  .map-shore { position: absolute; left: 0; bottom: 0; width: 535px; height: 330px; }
  .market-scene { position: absolute; left: 0; bottom: 0; width: 535px; height: 400px; }

  .card-head { position: absolute; left: 0; right: 0; top: 46px; text-align: center; }
  .card-title {
    font-family: "Baloo 2", sans-serif; font-weight: 800; color: var(--orange);
    font-size: 100px; line-height: 1; letter-spacing: -2px;
    transform: scaleX(.8); transform-origin: center;
  }
  .card-subtitle {
    font-family: "Patrick Hand SC", sans-serif; font-weight: 400; font-size: 37px; line-height: 1;
    margin-top: -6px;
  }
  .card-facts { margin-top: 6px; font-size: 16.5px; line-height: 19.5px; letter-spacing: -.2px; }

  .card-body {
    position: absolute; width: 442px; font-size: 21.5px; line-height: 34.4px;
    text-align: justify; letter-spacing: -.8px;
  }
  .rack-card--plain .card-body { left: 50px; top: 312px; }
  .rack-card--photo .card-body { left: 46px; top: 291px; text-align-last: left; }
  .card-note { position: absolute; left: 0; right: 0; top: 653px; text-align: center; font-size: 21.5px; letter-spacing: -.8px; }

  .map-pin { position: absolute; width: 20px; height: 26px; }

  .brand-mark {
    position: absolute; left: 0; right: 0; display: flex; align-items: center;
    justify-content: center; gap: 14px;
  }
  .rack-card--plain .brand-mark { bottom: 50px; }
  .rack-card--photo .brand-mark { bottom: 40px; }
  .brand-dot { width: 58px; height: 58px; border-radius: 50%; background: var(--orange); }
  .brand-name { font-size: 30px; color: var(--brand-grey); letter-spacing: -.5px; }
</style>
</head>
<body>

<svg width="0" height="0" style="position:absolute">
  <symbol id="pin" viewBox="0 0 20 26">
    <path d="M10 1a8.5 8.5 0 0 0-8.5 8.5C1.5 16 10 25 10 25s8.5-9 8.5-15.5A8.5 8.5 0 0 0 10 1z" fill="none" stroke="#f26522" stroke-width="2.6"/>
    <circle cx="10" cy="9.5" r="3" fill="none" stroke="#f26522" stroke-width="2.4"/>
  </symbol>
</svg>

<section class="rack-card rack-card--plain">
  <div class="city-map" role="img" aria-label="Faint grey street map of Setúbal's waterfront"></div>
  <svg class="map-shore" viewBox="0 0 535 330" preserveAspectRatio="none" aria-hidden="true">
    <path d="M0 330 L0 290 C120 200 240 120 330 80 C400 50 470 20 535 0 L535 330 Z" fill="var(--paper)"/>
  </svg>

  <header class="card-head">
    <h1 class="card-title">SETÚBAL</h1>
    <p class="card-subtitle">TRADITION AND TODAY</p>
    <p class="card-facts">Duration: 4 hours<br>+351 265 847 390<br>www.brisklanepasseios.com</p>
  </header>

  <p class="card-body">Experience the culinary delights of Setubal, Portugal with a walking food tour around our waterfront village. Discover the Mercado do Salgueiral, voted one of the world’s best markets by Daily Meridian, and indulge in local wines and dishes. Prepare for a calm stroll on flat streets.</p>
  <p class="card-note">No hills to climb on this tour.</p>

  <svg class="map-pin" style="left:384px;top:624px"><use href="#pin"/></svg>
  <svg class="map-pin" style="left:287px;top:709px"><use href="#pin"/></svg>
  <svg class="map-pin" style="left:396px;top:725px"><use href="#pin"/></svg>
  <svg class="map-pin" style="left:40px;top:864px"><use href="#pin"/></svg>

  <div class="brand-mark">
    <span class="brand-dot"></span>
    <span class="brand-name">Brisk Lane Passeios</span>
  </div>
</section>

<section class="rack-card rack-card--photo">
  <div class="city-map" role="img" aria-label="Faint grey street map of Setúbal's waterfront"></div>
  <svg class="market-scene" viewBox="0 0 535 400" preserveAspectRatio="none" role="img" aria-label="Faded photo of the bustling market hall with shoppers and statues">
    <defs>
      <linearGradient id="marketTone" x1="0" y1="0" x2="0" y2="1">
        <stop offset="0" stop-color="var(--photo-top)"/>
        <stop offset=".5" stop-color="var(--photo-mid)"/>
        <stop offset="1" stop-color="var(--photo-low)"/>
      </linearGradient>
    </defs>
    <path d="M0 400 L0 330 C90 210 180 90 300 20 C360 5 440 0 535 0 L535 400 Z" fill="url(#marketTone)"/>
  </svg>

  <header class="card-head">
    <h1 class="card-title">SETÚBAL</h1>
    <p class="card-subtitle">TRADITION AND TODAY</p>
    <p class="card-facts">Duration: 4 hours<br>+351 265 847 390<br>www.brisklanepasseios.com</p>
  </header>

  <p class="card-body">Experience the culinary delights of Setubal, Portugal with a walking food tour around our waterfront village. Discover the Mercado do Salgueiral, voted one of the world’s best markets by Daily Meridian, and indulge in local wines and dishes. Prepare for a calm stroll on flat streets.<br>No hills to climb on this tour.</p>

  <svg class="map-pin" style="left:342px;top:577px"><use href="#pin"/></svg>
  <svg class="map-pin" style="left:262px;top:648px"><use href="#pin"/></svg>
  <svg class="map-pin" style="left:353px;top:661px"><use href="#pin"/></svg>
  <svg class="map-pin" style="left:54px;top:778px"><use href="#pin"/></svg>

  <div class="brand-mark">
    <span class="brand-dot"></span>
    <span class="brand-name">Brisk Lane Passeios</span>
  </div>
</section>

</body>
</html>
```